Building Certification Company needs a professional letterhead and report template

We are a modern company within an ageing industry. Our industry is responsible for life safety aspects of the built environment, we ensure buildings are safe and fit for occupation.

We use letterhead and reports everyday, we need a smart and professional letterhead that reflects the serious nature of the work we do. We also require a report template of the same ilk.

Target Market(s)

Our target market will consist mainly of professional architects, developers and construction companies.

Industry/Entity Type

Industry

Requirements
Must have
• The letterhead must have:-
Our logo
Our company details, including address, website, email, phone

Address - Suite 208 / 45 Harwick Lane Dunmore NSW 2100

Website - www.quillstonecompliance.example.au

Email - info@qsc.example.au

Phone - 02 5550 3846

The report template must have:-
A title page, which is to incorporate our logo or an aspect of our logo, get creative people.

```html
<!DOCTYPE html>
<html lang="en">
<head>
<meta charset="utf-8">
<title>Quillstone Compliance – Letterhead</title>
<link rel="stylesheet" href="https://fonts.googleapis.com/css2?family=Arimo:wght@400;500&display=swap">
<style>
  :root {
    --brand-blue: #2340e8;
    --text-blue: #2c4ac4;
    --mark-grey: #e3e8ea;
    --mark-blue: #e2e7fb;
    --paper: #ffffff;
  }
  * { margin: 0; padding: 0; box-sizing: border-box; }
  html, body { width: 850px; height: 1200px; overflow: hidden; background: var(--paper); }
  .letterhead {
    position: relative;
    width: 850px;
    height: 1200px;
    border: 1px solid var(--brand-blue);
    font-family: "Arimo", Helvetica, Arial, sans-serif;
    color: var(--text-blue);
    overflow: hidden;
  }
  .top-band { position: absolute; top: 0; height: 49px; background: var(--brand-blue); }
  .top-band--left { left: 0; width: 516px; }
  .top-band--right { left: 778px; right: 0; }
  .brand {
    position: absolute;
    top: 62px;
    right: 84px;
    display: flex;
    align-items: center;
    gap: 12px;
  }
  .brand__square { width: 36px; height: 36px; background: var(--brand-blue); }
  .brand__name {
    font-size: 23px;
    font-weight: 500;
    letter-spacing: 1.5px;
    color: var(--brand-blue);
    line-height: 1.05;
    text-transform: uppercase;
  }
  .website {
    position: absolute;
    top: 137px;
    right: 84px;
    font-size: 14.5px;
    letter-spacing: -0.2px;
  }
  .backdrop {
    position: absolute;
    left: 143px;
    top: 352px;
    width: 543px;
    height: 466px;
    display: flex;
    flex-direction: column;
    align-items: center;
    justify-content: center;
    gap: 34px;
  }
  .backdrop__square { width: 150px; height: 150px; background: var(--mark-grey); }
  .backdrop__name {
    font-size: 44px;
    font-weight: 500;
    letter-spacing: 3px;
    text-transform: uppercase;
    color: var(--mark-blue);
    text-align: center;
    line-height: 1.1;
  }
  .contact {
    position: absolute;
    right: 73px;
    top: 1072px;
    text-align: right;
    font-size: 14px;
    line-height: 17px;
  }
  .contact__gap { margin-right: 10px; }
</style>
</head>
<body>
  <main class="letterhead">
    <div class="top-band top-band--left"></div>
    <div class="top-band top-band--right"></div>

    <header class="brand">
      <span class="brand__square"></span>
      <span class="brand__name">Quillstone<br>Compliance</span>
    </header>
    <p class="website">www.quillstonecompliance.example.au</p>

    <div class="backdrop" aria-hidden="true">
      <span class="backdrop__square"></span>
      <span class="backdrop__name">Quillstone<br>Compliance</span>
    </div>

    <footer class="contact">
      <p>Suite 208 / 45</p>
      <p>Harwick Lane Dunmore NSW 2100</p>
      <p><span class="contact__gap">Email - info@qsc.example.au</span> Phone - 02 5550 3846</p>
    </footer>
  </main>
</body>
</html>
```